One Page Brochure for Metal Recycling Company

We are a scrap metal recycling company and is looking for a one page, one sided brochure A4 size for our upcoming marketing campaign.

This brochure will be mass send to alot of prospective client and we would like it to be professional, but clear, simple and engaging.

We would like to have information on the brochure mainly 1) the type of materials we buy and 2) the service we provide

1) Material
- Scrap Aluminium
- Scrap Stainless Steel
- Scrap Alloy
- Scrap Copper / Brass
- Scrap Iron
- Obselete/Scrap Machinery
- Surplus Material

2) Service
- Prompt & Immediate Payment
- On site weighing
- Free Collection
- Free bin for disposal
- Waste disposal

Etc etc.

Our website is www.tanbokleong.com

Attached our logo and also our previous brochure design for reference.

Target Market(s)

Industrial customer

Industry/Entity Type

It Company

Requirements
Must have
• Our products and our services provide

```html
<!DOCTYPE html>
<html lang="en">
<head>
<meta charset="utf-8">
<title>Tan Bok Leong Recycling – Brochure</title>
<link href="https://fonts.googleapis.com/css2?family=Roboto+Condensed:wght@400;700&display=swap" rel="stylesheet">
<style>
  :root{
    --gold:#c9961e;
    --gold-soft:#e9c77e;
    --orange:#ef9a4a;
    --band-grey:#7d7d7d;
    --label-grey:#6e6e6e;
    --paper:#ffffff;
    --backdrop:#e6e6e6;
  }
  *{box-sizing:border-box;margin:0;padding:0}
  html,body{width:1194px;height:1200px;overflow:hidden;background:var(--backdrop)}
  body{font-family:"Roboto Condensed",Arial,sans-serif}
  .brochure{position:absolute;left:188px;top:20px;width:818px;height:1160px;background:var(--paper);overflow:hidden}
  .top-rule{position:absolute;left:0;top:0;width:100%;height:6px;background:var(--gold)}
  .hero{position:absolute;left:0;top:6px;width:100%;height:334px;
    background:linear-gradient(100deg,#2f6f95 0%,#5fa3c9 35%,#dfe9ef 65%,#f4f4f2 80%),#6a8aa0}
  .hero::after{content:"";position:absolute;left:0;bottom:0;width:100%;height:55%;
    background:linear-gradient(180deg,rgba(90,80,70,0) 0%,#6b5a48 45%,#3c3128 100%)}
  .brand{position:absolute;right:42px;top:24px;text-align:right;z-index:2}
  .brand-mark{display:inline-block;width:52px;height:52px;border:3px solid var(--gold);margin-right:48px}
  .brand-name{font-size:22px;font-weight:700;letter-spacing:2px;color:var(--gold);margin-top:10px}
  .brand-sub{font-size:11px;font-weight:700;letter-spacing:2px;color:#555}
  .headline{position:absolute;right:40px;top:250px;text-align:right;font-weight:700;font-size:38px;line-height:42px;z-index:2}
  .headline .l1{color:#fff}
  .headline .l2{color:var(--gold)}
  .section-band{position:absolute;left:0;width:100%;color:#fff;font-weight:700;font-size:25px;text-align:center}
  .materials-band{top:340px;height:40px;line-height:40px;background:var(--gold)}
  .service-band{top:826px;height:32px;line-height:32px;background:var(--band-grey);text-align:left;padding-left:193px;font-size:24px}
  .material{position:absolute;width:190px;margin-left:-95px;text-align:center}
  .material svg{display:block;margin:0 auto}
  .material-label{font-size:16px;color:var(--label-grey);font-weight:700;margin-top:6px}
  .service{position:absolute;width:150px;margin-left:-75px;text-align:center}
  .service-label{font-size:13px;font-weight:700;color:var(--label-grey);margin-top:10px;line-height:16px}
  .service-divider{position:absolute;width:1px;height:74px;background:#dcdcdc}
  .contact-panel{position:absolute;left:0;top:0}
  .contact{position:absolute;left:610px;font-size:14px;color:#3b2a10;display:flex;gap:8px;line-height:16px}
  .contact svg{flex:none;margin-top:1px}
  .bottom-rule{position:absolute;left:0;bottom:0;width:600px;height:7px;background:#9a9a9a}
</style>
</head>
<body>
<main class="brochure">
  <div class="top-rule"></div>
  <div class="hero" role="img" aria-label="Photo of two workers in hard hats at a scrap metal yard with an excavator and piles of scrap"></div>
  <div class="brand">
    <span class="brand-mark"></span>
    <div class="brand-name">TAN BOK LEONG</div>
    <div class="brand-sub">RECYCLING</div>
  </div>
  <h1 class="headline"><span class="l1">INDUSTRY LEADER</span><br><span class="l2">IN METAL RECYCLING</span></h1>

  <h2 class="section-band materials-band">TYPE OF MATERIALS WE BUY</h2>

  <svg width="0" height="0" style="position:absolute">
    <defs>
      <symbol id="ring" viewBox="0 0 190 160">
        <path d="M38 72 A58 58 0 1 1 152 88" fill="none" stroke="#c9961e" stroke-width="7"/>
        <path d="M152 88 A58 58 0 1 1 38 72" fill="none" stroke="#c9961e" stroke-width="7" stroke-dasharray="0 30 400"/>
        <polygon points="24,70 52,70 38,88" fill="#c9961e"/>
        <polygon points="138,90 166,90 152,72" fill="#c9961e"/>
      </symbol>
    </defs>
  </svg>

  <div class="material" style="left:151px;top:408px">
    <svg width="190" height="150" viewBox="0 0 190 160"><circle cx="95" cy="80" r="54" fill="#9aa0a6" role="img" aria-label="Photo of baled aluminium scrap"/><use href="#ring"/></svg>
    <div class="material-label">Scrap Aluminium</div>
  </div>
  <div class="material" style="left:424px;top:408px">
    <svg width="190" height="150" viewBox="0 0 190 160"><circle cx="95" cy="80" r="54" fill="#8f959b" role="img" aria-label="Photo of baled stainless steel scrap"/><use href="#ring"/></svg>
    <div class="material-label">Scrap Stainless Steel</div>
  </div>
  <div class="material" style="left:671px;top:408px">
    <svg width="190" height="150" viewBox="0 0 190 160"><circle cx="95" cy="80" r="54" fill="#858c96" role="img" aria-label="Photo of baled alloy scrap"/><use href="#ring"/></svg>
    <div class="material-label">Scrap Alloy</div>
  </div>

  <div class="material" style="left:117px;top:605px">
    <svg width="190" height="150" viewBox="0 0 190 160"><circle cx="95" cy="80" r="54" fill="#a07860" role="img" aria-label="Photo of copper wire and brass scrap"/><use href="#ring"/></svg>
    <div class="material-label">Scrap Copper / Brass</div>
  </div>
  <div class="material" style="left:316px;top:605px">
    <svg width="190" height="150" viewBox="0 0 190 160"><circle cx="95" cy="80" r="54" fill="#7e8088" role="img" aria-label="Photo of mixed iron scrap parts"/><use href="#ring"/></svg>
    <div class="material-label">Scrap Iron</div>
  </div>
  <div class="material" style="left:514px;top:605px">
    <svg width="190" height="150" viewBox="0 0 190 160"><circle cx="95" cy="80" r="54" fill="#4a4d55" role="img" aria-label="Photo of obsolete engine machinery"/><use href="#ring"/></svg>
    <div class="material-label">Obselete/Scrap Machinery</div>
  </div>
  <div class="material" style="left:713px;top:605px">
    <svg width="190" height="150" viewBox="0 0 190 160"><circle cx="95" cy="80" r="54" fill="#b0ada4" role="img" aria-label="Photo of a coil of surplus wire"/><use href="#ring"/></svg>
    <div class="material-label">Surplus Material</div>
  </div>

  <h2 class="section-band service-band">SERVICE</h2>

  <svg class="contact-panel" width="818" height="1160" viewBox="0 0 818 1160">
    <defs>
      <linearGradient id="panelFill" x1="0" y1="0" x2="1" y2="0">
        <stop offset="0" stop-color="#d4950f"/><stop offset="1" stop-color="#ef9a4a"/>
      </linearGradient>
      <radialGradient id="iconFill" cx="0.4" cy="0.35" r="0.7">
        <stop offset="0" stop-color="#f6dfae"/><stop offset="1" stop-color="#dcae55"/>
      </radialGradient>
    </defs>
    <polygon points="818,860 440,1037 583,1160 818,1160" fill="url(#panelFill)"/>
    <g fill="url(#iconFill)">
      <circle cx="98" cy="907" r="31"/><circle cx="234" cy="907" r="31"/><circle cx="368" cy="907" r="31"/>
      <circle cx="98" cy="1043" r="31"/><circle cx="234" cy="1043" r="31"/>
    </g>
    <g fill="#9a6a10">
      <rect x="88" y="890" width="18" height="30" rx="3"/><rect x="91" y="894" width="12" height="18" fill="#f1d59a"/>
      <path d="M220 902h8l6-14c4 0 6 3 5 7l-2 7h10c3 0 5 3 4 6l-4 14c-1 2-3 3-5 3h-22z"/><rect x="214" y="902" width="5" height="23"/>
      <rect x="356" y="897" width="24" height="3"/><rect x="364" y="893" width="8" height="4"/><path d="M358 902h20l-2 22h-16z"/>
      <path d="M88 1033h20l6 24h-32z"/><circle cx="98" cy="1029" r="5" fill="none" stroke="#9a6a10" stroke-width="3"/>
      <circle cx="243" cy="1025" r="4"/><path d="M240 1031h6l3 24h-4l-2-10-3 10h-4z"/><path d="M222 1037h14l-2 18h-10z"/>
    </g>
    <text x="98" y="1048" font-family="Roboto Condensed, Arial, sans-serif" font-size="10" font-weight="700" fill="#fff" text-anchor="middle">KG</text>
  </svg>

  <div class="service" style="left:98px;top:945px"><div class="service-label">Prompt &amp; Immediate<br>Payment</div></div>
  <div class="service" style="left:234px;top:945px"><div class="service-label">Free Collection</div></div>
  <div class="service" style="left:368px;top:945px"><div class="service-label">Free bin for disposal</div></div>
  <div class="service" style="left:98px;top:1081px"><div class="service-label">On site weighing</div></div>
  <div class="service" style="left:234px;top:1081px"><div class="service-label">Waste disposal</div></div>
  <div class="service-divider" style="left:170px;top:875px"></div>
  <div class="service-divider" style="left:301px;top:875px"></div>
  <div class="service-divider" style="left:170px;top:1011px"></div>

  <address class="contact-list" style="font-style:normal">
    <div class="contact" style="top:991px">
      <svg width="14" height="16" viewBox="0 0 14 16"><path d="M7 0a6 6 0 0 0-6 6c0 4 6 10 6 10s6-6 6-10a6 6 0 0 0-6-6zm0 8.5a2.5 2.5 0 1 1 0-5 2.5 2.5 0 0 1 0 5z" fill="#3b2a10"/></svg>
      <span>27, Benoi Crescent,<br>Singapore 629981</span>
    </div>
    <div class="contact" style="top:1035px">
      <svg width="14" height="14" viewBox="0 0 14 14"><path d="M3 1l2 3-1 2c1 2 2 3 4 4l2-1 3 2-1 2C6 13 1 8 1 2z" fill="#3b2a10"/></svg>
      <span>(+65) 9000 4321</span>
    </div>
    <div class="contact" style="top:1060px">
      <svg width="14" height="12" viewBox="0 0 14 12"><rect x="0.5" y="1.5" width="13" height="9" fill="none" stroke="#3b2a10"/><path d="M1 2l6 5 6-5" fill="none" stroke="#3b2a10"/></svg>
      <span>sales@tanbokleong.com</span>
    </div>
    <div class="contact" style="top:1083px">
      <svg width="14" height="14" viewBox="0 0 14 14"><circle cx="7" cy="7" r="6" fill="none" stroke="#3b2a10"/><ellipse cx="7" cy="7" rx="2.5" ry="6" fill="none" stroke="#3b2a10"/><path d="M1 7h12" stroke="#3b2a10"/></svg>
      <span>www.tanbokleong.com</span>
    </div>
  </address>

  <div class="bottom-rule"></div>
</main>
</body>
</html>
```